"Velvet Petal Hour" Fashion Show Invitation design

We need an invitation design for our fashion show with the theme "Velvet Petal Hour"

the design will be the cover of the invitation, save the date cards, program etc

We are a philanthropic organization. Would like to incorporate florals, jewel tones or pastels etc... not sure if theres a way O or need) to incorporate fashion into that in an elegant way.

Text should read The Carrowfield Circle Presents "Velvet Petal Hour"
Updates

I'm looking for the design/image for the cover of our invitation- The only text needed is The Carrowfield Circle Presents Velvet Petal Hour I'm looking for feminine, elegant, florals etc...

Font styles to use
Serif
Decorative
Script

Colors
b768aa
e667a6
85cae6

Requirements
Must have
• jewel tones or pastels, flowers,
Nice to have
• fashion?

```html
<!DOCTYPE html>
<html lang="en">
<head>
<meta charset="UTF-8">
<title>The Carrowfield Circle Presents Velvet Petal Hour</title>
<link rel="stylesheet" href="https://fonts.googleapis.com/css2?family=Pinyon+Script&family=Playfair+Display:wght@700;800&display=swap">
<style>
  :root {
    --sky: #85cae6;
    --sky-deep: #6fbde0;
    --rose-pink: #e667a6;
    --orchid: #b768aa;
    --periwinkle: #7f8fdc;
    --blush: #f4c6e0;
    --lily: #f7f4f8;
    --lily-tint: #cfeee8;
    --ink: #2f2426;
    --white: #ffffff;
  }
  * { margin: 0; padding: 0; box-sizing: border-box; }
  html, body { width: 800px; height: 1200px; overflow: hidden; background: var(--sky); }

  .invitation-cover {
    position: relative;
    width: 800px;
    height: 1200px;
    overflow: hidden;
    background: radial-gradient(ellipse at 50% 45%, var(--sky) 0%, var(--sky-deep) 100%);
  }

  .floral {
    position: absolute;
    border-radius: 50%;
  }
  .floral--rose {
    background: radial-gradient(circle at 45% 45%, var(--periwinkle) 0%, var(--orchid) 45%, var(--rose-pink) 75%, rgba(230,103,166,0) 100%);
    opacity: 0.85;
  }
  .floral--peony {
    background: radial-gradient(circle at 50% 50%, var(--lily) 0%, var(--blush) 50%, rgba(244,198,224,0) 100%);
    opacity: 0.9;
  }
  .floral--lily {
    background: radial-gradient(circle at 50% 50%, var(--lily-tint) 0%, var(--lily) 40%, rgba(247,244,248,0) 100%);
  }

  .rose-top-left { left: 30px; top: 50px; width: 290px; height: 270px; }
  .rose-right { left: 620px; top: 130px; width: 260px; height: 400px; opacity: 0.6; }
  .rose-bottom-left { left: 10px; top: 860px; width: 380px; height: 360px; }
  .peony-top { left: 340px; top: -60px; width: 290px; height: 180px; }
  .peony-left { left: -60px; top: 370px; width: 200px; height: 280px; }
  .peony-bottom-right { left: 480px; top: 760px; width: 300px; height: 350px; }
  .lily-top-left { left: -50px; top: -50px; width: 150px; height: 140px; }
  .lily-top-right { left: 600px; top: -40px; width: 240px; height: 200px; }
  .lily-right { left: 660px; top: 520px; width: 180px; height: 420px; }
  .lily-left { left: -50px; top: 720px; width: 210px; height: 260px; }
  .lily-bottom { left: 440px; top: 1040px; width: 300px; height: 200px; }
  .lily-bottom-right { left: 720px; top: 1100px; width: 140px; height: 140px; }

  .silhouette {
    position: absolute;
    left: 240px; top: 240px;
    width: 400px; height: 650px;
    border-radius: 45% 45% 40% 40%;
    background: radial-gradient(ellipse at 50% 50%, rgba(183,104,170,0.35) 0%, rgba(183,104,170,0) 70%);
  }

  .frame {
    position: absolute;
    left: 20px; top: 20px;
    width: 760px; height: 1160px;
    border: 13px solid rgba(230,103,166,0.65);
  }

  .heading {
    position: absolute;
    left: 0; top: 168px;
    width: 800px;
    text-align: center;
    color: var(--white);
    font-family: "Playfair Display", Georgia, serif;
    font-weight: 800;
    text-shadow: 0 1px 4px rgba(80,40,90,0.25);
  }
  .heading__host { font-size: 45px; letter-spacing: 0.5px; line-height: 1.1; }
  .heading__presents { font-size: 26px; letter-spacing: 0.5px; margin-top: 4px; }

  .title {
    position: absolute;
    left: 0; top: 300px;
    width: 800px;
    text-align: center;
    color: var(--ink);
    font-family: "Pinyon Script", cursive;
    font-weight: 400;
    font-size: 168px;
    line-height: 240px;
    text-shadow: 0 3px 6px rgba(40,30,50,0.25);
  }
  .title__line { display: block; }
</style>
</head>
<body>
  <main class="invitation-cover">
    <div class="silhouette" role="img" aria-label="Faint dress form silhouette behind the title"></div>

    <div class="floral floral--rose rose-top-left" role="img" aria-label="Pink and blue rose"></div>
    <div class="floral floral--rose rose-right" role="img" aria-label="Soft pink rose at the right edge"></div>
    <div class="floral floral--rose rose-bottom-left" role="img" aria-label="Large pink and periwinkle rose"></div>
    <div class="floral floral--peony peony-top" role="img" aria-label="Pale pink peony"></div>
    <div class="floral floral--peony peony-left" role="img" aria-label="Pale pink peony at the left edge"></div>
    <div class="floral floral--peony peony-bottom-right" role="img" aria-label="Blush peony"></div>
    <div class="floral floral--lily lily-top-left" role="img" aria-label="White lily"></div>
    <div class="floral floral--lily lily-top-right" role="img" aria-label="White lily"></div>
    <div class="floral floral--lily lily-right" role="img" aria-label="White lily at the right edge"></div>
    <div class="floral floral--lily lily-left" role="img" aria-label="White lily at the left edge"></div>
    <div class="floral floral--lily lily-bottom" role="img" aria-label="White lily"></div>
    <div class="floral floral--lily lily-bottom-right" role="img" aria-label="White lily"></div>

    <div class="frame"></div>

    <header class="heading">
      <p class="heading__host">THE CARROWFIELD CIRCLE</p>
      <p class="heading__presents">PRESENTS</p>
    </header>

    <h1 class="title">
      <span class="title__line">Velvet</span>
      <span class="title__line">Petal</span>
      <span class="title__line">Hour</span>
    </h1>
  </main>
</body>
</html>
```